Business Card Design Project

We consult with hotels on setting rates and maximizing a revenue strategy

Industry/Entity Type

Business

Contact Information for Business Card

I am not sure what I want. Our company offers high level consulting to hotels around the country but we are also laid back. I would like something that is professional but also shows the laid back side

```html
<!DOCTYPE html>
<html lang="en">
<head>
<meta charset="utf-8">
<title>Harborline – Business Card</title>
<link href="https://fonts.googleapis.com/css2?family=Lato:wght@400;700;900&display=swap" rel="stylesheet">
<style>
  :root {
    --bg: #2a2a2a;
    --card: #fbfbfa;
    --teal: #2f7f79;
    --brown: #3b2c26;
    --ink: #1f1f1f;
    --muted: #333333;
  }
  * { margin: 0; padding: 0; box-sizing: border-box; }
  html, body {
    width: 1200px; height: 873px; overflow: hidden;
    background: var(--bg);
    font-family: "Lato", sans-serif;
  }
  .stage {
    position: relative; width: 1200px; height: 873px;
    display: flex; align-items: center; justify-content: center; gap: 40px;
  }
  .card {
    position: relative; width: 540px; height: 309px;
    background: var(--card); overflow: hidden;
  }
  .card__band {
    position: absolute; left: 0; bottom: 0; width: 540px; height: 40px;
  }
  /* Back side */
  .brand-back {
    position: absolute; left: 0; right: 0; top: 112px;
    display: flex; align-items: center; justify-content: center; gap: 14px;
  }
  .brand-back__mark { width: 18px; height: 18px; background: var(--teal); }
  .brand-back__name {
    font-weight: 900; font-size: 52px; letter-spacing: 3px; color: var(--brown);
  }
  /* Front side */
  .brand-front {
    position: absolute; left: 150px; top: 70px;
    display: flex; align-items: center; gap: 10px;
  }
  .brand-front__mark { width: 14px; height: 14px; background: var(--teal); }
  .brand-front__name {
    font-weight: 900; font-size: 34px; letter-spacing: 1px; color: var(--brown);
  }
  .person {
    position: absolute; right: 34px; top: 150px; text-align: right;
  }
  .person__name { font-weight: 700; font-size: 17px; color: var(--ink); }
  .person__title { font-weight: 400; font-size: 15px; color: var(--muted); margin-top: 3px; }
  .contact-tab {
    position: absolute; left: 0; top: 196px; width: 42px; height: 96px;
    background: var(--teal); border-radius: 0 8px 8px 0;
    display: flex; flex-direction: column; align-items: center; justify-content: space-around;
    padding: 8px 0;
  }
  .contact-tab svg { width: 18px; height: 16px; fill: #fff; }
  .contact-list {
    position: absolute; left: 58px; top: 202px; list-style: none;
  }
  .contact-list li {
    font-weight: 700; font-size: 15px; color: var(--ink); line-height: 27px;
  }
</style>
</head>
<body>
<main class="stage">

  <section class="card card--back" aria-label="Card back">
    <div class="brand-back">
      <span class="brand-back__mark"></span>
      <span class="brand-back__name">HARBORLINE</span>
    </div>
    <svg class="card__band" viewBox="0 0 540 40" aria-hidden="true">
      <path d="M340 24 Q350 12 368 12 L540 12 L540 40 L340 40 Z" fill="var(--teal)"/>
      <rect x="0" y="30" width="540" height="10" fill="var(--brown)"/>
    </svg>
  </section>

  <section class="card card--front" aria-label="Card front">
    <div class="brand-front">
      <span class="brand-front__mark"></span>
      <span class="brand-front__name">HARBORLINE</span>
    </div>

    <div class="person">
      <p class="person__name">Dana Whitley</p>
      <p class="person__title">Regional Revenue Manager</p>
    </div>

    <div class="contact-tab" aria-hidden="true">
      <svg viewBox="0 0 18 16"><path d="M2 5c0-2 3-3 7-3s7 1 7 3v1h-4V4.5c-2-.6-4-.6-6 0V6H2z"/><path d="M4 8h10l2 7H2z"/></svg>
      <svg viewBox="0 0 18 16"><rect x="5" y="1" width="8" height="4"/><rect x="1" y="6" width="16" height="6" rx="1"/><rect x="5" y="10" width="8" height="5"/></svg>
      <svg viewBox="0 0 18 16"><path d="M1 3h16v10H1z M2 4l7 5 7-5" fill="none" stroke="#fff" stroke-width="1.6"/></svg>
    </div>
    <ul class="contact-list">
      <li>503-555-0142</li>
      <li>503-555-0187</li>
      <li>Dana@HarborlineRMS.com</li>
    </ul>

    <svg class="card__band" viewBox="0 0 540 40" aria-hidden="true">
      <path d="M340 24 Q350 12 368 12 L540 12 L540 40 L340 40 Z" fill="var(--teal)"/>
      <rect x="0" y="30" width="540" height="10" fill="var(--brown)"/>
    </svg>
  </section>

</main>
</body>
</html>
```